Website for new dental office

I am Dr. Colin Marsh and am building a new dental practice. I specialize in general dentistry. I am young and have a higher end dental practice incorporating very new technologies and would like my website to reflect that. As many dental patients are older, the website must be very easy to navigate. I would like patients to be able to request appointments, and will eventually add on patient information forms (the health history, etc, that you normally fill out in the practice) from my practice management software, so leave an area for that.

Industry/Entity Type

Building

```html
<!DOCTYPE html>
<html lang="en">
<head>
<meta charset="utf-8">
<title>Dr. Colin Marsh – Dental Practice</title>
<link href="https://fonts.googleapis.com/css2?family=Bree+Serif&family=Open+Sans:wght@400;600&display=swap" rel="stylesheet">
<style>
:root{
  --sky:#3fb0e4;
  --blue:#1383d4;
  --royal:#3a53a4;
  --navy:#2b4a8e;
  --indigo:#3456a8;
  --map:#4aa8de;
  --footer:#565656;
  --grey-text:#8a8a8a;
  --light:#d9d9d9;
  --white:#ffffff;
}
*{margin:0;padding:0;box-sizing:border-box}
html,body{width:746px;height:1200px;overflow:hidden;background:var(--white)}
body{position:relative;font-family:"Open Sans",sans-serif;color:var(--grey-text)}
.abs{position:absolute}
.slab{font-family:"Bree Serif",serif}

/* header */
.brand{left:124px;top:16px;display:flex;align-items:center;gap:6px;color:var(--sky);font-family:"Bree Serif",serif;font-size:17px}
.brand .dot{width:14px;height:14px;border-radius:50%;background:var(--sky)}
.call{left:501px;top:14px;color:var(--blue)}
.call small{display:block;font-size:6.5px;letter-spacing:.2px}
.call strong{display:block;font-family:"Bree Serif",serif;font-weight:400;font-size:16px;margin-top:1px}
.header-rule{left:0;top:55px;width:746px;height:1px;background:#efefef}

/* hero */
.hero-photo{left:360px;top:58px;width:386px;height:252px;background:radial-gradient(ellipse at 60% 55%,#f3c9a6 0%,#e7b489 35%,#b9d47a 60%,#ffffff 85%)}
.welcome{left:122px;top:160px;width:168px;text-align:center}
.welcome h1{font-family:"Bree Serif",serif;font-weight:400;color:var(--sky);font-size:33px;line-height:1}
.welcome h2{font-family:"Bree Serif",serif;font-weight:400;color:var(--royal);font-size:20px;line-height:1.1;margin-top:2px}
.welcome p{font-size:6.5px;line-height:1.25;margin-top:3px}

/* nav */
.nav{left:0;top:310px;width:746px;height:29px;background:var(--royal)}
.nav ul{list-style:none;position:absolute;left:124px;top:0;display:flex}
.nav li{width:100px;height:29px;line-height:29px;text-align:center;font-family:"Bree Serif",serif;font-size:8.5px;color:var(--white);border-right:1px solid #34499a}
.nav li.active{background:var(--light);color:var(--royal)}

/* appointment */
.appt{left:0;top:339px;width:746px;height:97px;background:var(--blue)}
.appt h3{position:absolute;left:0;top:13px;width:746px;text-align:center;font-family:"Bree Serif",serif;font-weight:400;color:var(--white);font-size:13.5px}
.appt .notch{position:absolute;left:368px;top:30px;width:0;height:0;border:5px solid transparent;border-top-color:var(--blue);border-bottom:0}
.field{position:absolute;background:var(--white);border:1px solid #c9d6e4;font-size:6px;color:#999;padding:3px 4px}
.btn-make{position:absolute;left:498px;top:43px;width:92px;height:42px;background:#d0d0d0;color:var(--blue);font-family:"Bree Serif",serif;font-size:11px;display:flex;align-items:center;justify-content:center;border-radius:1px}

/* services */
.section-title{left:0;top:458px;width:746px;text-align:center;font-family:"Bree Serif",serif;color:var(--royal);font-size:13px}
.tiles{left:124px;top:486px;width:498px;height:69px;display:flex}
.tile{flex:1;position:relative;display:flex;flex-direction:column;align-items:center;color:var(--white);font-family:"Bree Serif",serif;font-size:8px}
.tile svg{margin-top:10px}
.tile span{position:absolute;top:53px}
.tile.t1{background:var(--sky)}
.tile.t2{background:var(--blue)}
.tile.t3{background:var(--indigo)}
.tile.t4{background:var(--navy)}
.tile.t1::after{content:"";position:absolute;left:58px;bottom:-5px;border:5px solid transparent;border-top-color:var(--sky);border-bottom:0}
.services-text{left:128px;top:578px;width:490px;text-align:center;font-size:6px;line-height:1.3}
.services-rule{left:124px;top:612px;width:498px;height:2px;background:#eef0f2}

/* portraits */
.portrait{position:absolute;top:650px;width:68px;height:68px;border-radius:50%;border:3px solid #e4f2ef}

/* location */
.locate{left:0;top:751px;width:746px;height:271px;background:radial-gradient(ellipse at 45% 45%,#5ab3e4 0%,var(--map) 60%,#43a0d8 100%)}
.address{left:130px;top:837px;color:var(--white);font-family:"Bree Serif",serif;font-size:10px;line-height:12.5px}
.orbit{left:0;top:751px}
.orbit-label{position:absolute;color:#e8f4fb;font-size:8.5px}

/* footer */
.footer{left:0;top:1022px;width:746px;height:148px;background:var(--footer)}
.foot-col{position:absolute;top:19px;width:124px;color:#e6e6e6}
.foot-col h4{font-family:"Bree Serif",serif;font-weight:400;color:var(--white);font-size:9.5px;padding-bottom:2px;border-bottom:2px solid #e6e6e6}
.foot-col p{font-size:6px;line-height:1.3;margin-top:4px}
.foot-brand{font-family:"Bree Serif",serif;color:#bfbfbf;font-size:17px;margin-top:14px;display:flex;align-items:center;gap:5px}
.foot-brand i{width:12px;height:12px;border-radius:50%;background:#bfbfbf;display:block}
.post{margin-top:10px!important}
.news-input{position:absolute;left:490px;width:132px;height:16px;background:var(--white)}
.btn-submit{position:absolute;left:563px;top:114px;width:58px;height:18px;background:var(--blue);color:var(--white);font-family:"Bree Serif",serif;font-size:6px;display:flex;align-items:center;justify-content:center}
.bottom-bar{left:0;top:1170px;width:746px;height:30px;background:var(--blue);color:#dcefff;font-size:6.5px;line-height:30px;padding-left:125px}
</style>
</head>
<body>

<header>
  <div class="abs brand"><i class="dot"></i>Dr. Colin Marsh</div>
  <div class="abs call"><small>CALL US TODAY</small><strong>0800-555-01-234</strong></div>
  <div class="abs header-rule"></div>
</header>

<section>
  <div class="abs hero-photo" role="img" aria-label="Photo of a smiling family of four"></div>
  <div class="abs welcome">
    <h1>WELCOME</h1>
    <h2>TO Dr.Colin Marsh</h2>
    <p>Lorem ipsum dolor sit amet, consectetuer adipiscing elit, sed diam nonummy nibh euismod tincidunt ut laoreet dolore....</p>
  </div>
</section>

<nav class="abs nav">
  <ul>
    <li class="active">SERVICES</li>
    <li>TERMS OF USE</li>
    <li>ABOUT US</li>
    <li>TESTIMONIALS</li>
    <li>CONTACT US</li>
  </ul>
</nav>

<section class="abs appt">
  <h3>MAKE AN APPIONMENT</h3>
  <span class="notch"></span>
  <div class="field" style="left:157px;top:43px;width:95px;height:17px">Name</div>
  <div class="field" style="left:259px;top:43px;width:95px;height:17px">Email</div>
  <div class="field" style="left:157px;top:67px;width:95px;height:17px">Subject</div>
  <div class="field" style="left:259px;top:67px;width:95px;height:17px">
    <svg class="abs" style="right:7px;top:4px" width="9" height="8" viewBox="0 0 9 8"><rect x=".5" y=".5" width="8" height="7" fill="none" stroke="#777"/><line x1="1" y1="3" x2="8" y2="3" stroke="#777"/></svg>
  </div>
  <div class="field" style="left:363px;top:43px;width:131px;height:42px">Message....</div>
  <div class="btn-make">MAKE NOW!</div>
</section>

<section>
  <div class="abs section-title">SERVICES</div>
  <div class="abs tiles">
    <div class="tile t1">
      <svg width="32" height="34" viewBox="0 0 32 34" fill="none" stroke="#fff" stroke-width="2.5">
        <circle cx="13" cy="19" r="8"/><circle cx="19" cy="14" r="8"/>
        <line x1="13" y1="27" x2="13" y2="33"/><line x1="10" y1="30" x2="16" y2="30"/>
        <line x1="25" y1="8" x2="30" y2="3"/><polyline points="25,3 30,3 30,8"/>
      </svg>
      <span>NONUMMY NIBH</span>
    </div>
    <div class="tile t2">
      <svg width="32" height="34" viewBox="0 0 32 34" fill="none" stroke="#fff" stroke-width="2.5">
        <path d="M4 30 C12 22 20 20 28 4"/><path d="M4 18 C12 10 20 16 28 12"/>
        <line x1="9" y1="24" x2="11" y2="15"/><line x1="15" y1="20" x2="17" y2="14"/><line x1="21" y1="15" x2="23" y2="12"/>
      </svg>
      <span>NONUMMY NIBH</span>
    </div>
    <div class="tile t3">
      <svg width="32" height="34" viewBox="0 0 32 34" fill="none" stroke="#fff" stroke-width="2.5">
        <line x1="16" y1="2" x2="16" y2="33"/><path d="M3 9 Q16 5 29 9"/>
        <path d="M11 14 Q21 17 11 21 Q21 24 13 28"/><path d="M21 14 Q11 17 21 21 Q11 24 19 28"/>
      </svg>
      <span>NONUMMY NIBH</span>
    </div>
    <div class="tile t4">
      <svg width="32" height="34" viewBox="0 0 32 34" fill="none" stroke="#fff" stroke-width="2.5">
        <path d="M5 10 L9 32 L23 32 L27 10 Z"/><line x1="13" y1="26" x2="24" y2="4"/><rect x="22" y="1" width="5" height="6" transform="rotate(27 24 4)"/>
      </svg>
      <span>NONUMMY NIBH</span>
    </div>
  </div>
  <p class="abs services-text">Lorem ipsum dolor sit amet, consectetuer adipiscing elit, sed diam nonummy nibh euismod tincidunt ut laoreet dolore magna aliquam erat volutpat. Ut wisi enim ad minim veniam, quis nostrud exerci tation ullamcorper suscipit lobortis nisl ut aliquip ex ea commodo consequat................</p>
  <div class="abs services-rule"></div>
</section>

<section>
  <div class="portrait" style="left:139px;background:radial-gradient(circle,#f2d8c4,#e9eef0)" role="img" aria-label="Photo of a dental assistant"></div>
  <div class="portrait" style="left:218px;background:radial-gradient(circle,#d9b195,#dfe3e6)" role="img" aria-label="Photo of a smiling young man"></div>
  <div class="portrait" style="left:298px;background:radial-gradient(circle,#d8b49a,#b7c9a0)" role="img" aria-label="Photo of a happy family"></div>
  <div class="portrait" style="left:377px;background:radial-gradient(circle,#e6ecef,#4d7fb8)" role="img" aria-label="Photo of the practice building"></div>
  <div class="portrait" style="left:457px;background:radial-gradient(circle,#d9ad8e,#8a5c3e)" role="img" aria-label="Photo of a smiling woman"></div>
  <div class="portrait" style="left:536px;background:radial-gradient(circle,#e3a06a,#9c2a14)" role="img" aria-label="Photo of a laughing patient"></div>
</section>

<section>
  <div class="abs locate" role="img" aria-label="Faint world map background"></div>
  <address class="abs address" style="font-style:normal">
    Linden street<br>04-118 Harbury<br>information: +48 700 100 200<br>appointments: +48 700 555 0199<br>email: hello@marshdental.example
  </address>
  <svg class="abs orbit" width="746" height="271" viewBox="0 0 746 271" fill="none" stroke="#ffffff" stroke-opacity=".85" stroke-width="1">
    <circle cx="470" cy="143" r="93"/>
    <circle cx="470" cy="143" r="74"/>
    <circle cx="470" cy="143" r="51"/>
    <circle cx="439" cy="106" r="7" fill="#e3e3e3" stroke="none"/>
    <circle cx="505" cy="176" r="7" fill="#e3e3e3" stroke="none"/>
    <circle cx="439" cy="212" r="7" fill="#e3e3e3" stroke="none"/>
  </svg>
  <span class="orbit-label" style="left:358px;top:838px">Contact Form</span>
  <span class="orbit-label" style="left:535px;top:921px">Zoom Out Map</span>
  <span class="orbit-label" style="left:358px;top:957px">Meet our team</span>
</section>

<footer class="abs footer">
  <div class="foot-col" style="left:125px">
    <h4>ABOUT US</h4>
    <div class="foot-brand"><i></i>Dr. Colin Marsh</div>
    <p>Dr. Colin Marsh auctor, nisi elit consequat ipsum, nec sagittis sem nibh id elit. Duis sed odio sit amet nibh vulputateUpdate: Website Theme Submission Requirements</p>
  </div>
  <div class="foot-col" style="left:308px">
    <h4>LATEST POSTS</h4>
    <p style="margin-top:12px">Update: Website Theme Submission Requirements</p>
    <p class="post">Does a well designed thumbnail increase your sales?</p>
    <p class="post">Brain Most Wanted - $5,000 Reward for the First 15 Hosting</p>
    <p class="post">Update: Website Theme Submission Requirements</p>
  </div>
  <div class="foot-col" style="left:494px">
    <h4>NEWSLETTER</h4>
    <p style="margin-top:12px">Dr. Colin Marsh auctor, nisi elit consequat ipsum, nec sagittis sem nibh id</p>
  </div>
  <div class="news-input" style="top:70px"></div>
  <div class="news-input" style="top:91px"></div>
  <div class="btn-submit">SUBMIT NOW</div>
</footer>

<div class="abs bottom-bar">© 2013 Marsh Dental, All Rights Reserved.</div>

</body>
</html>
```